velmorquay.com - a boating experience in fenwick island delaware.

Home page content
Embark on an unparalleled voyage on our vessel "Brisk Lantern Tide" and discover the epitome of luxury boating. Indulge in the beauty of the Fenwick Island, Delaware, and the Ocean City, Maryland area while experiencing the unparalleled comfort and opulence of our Quellin 34 cabin vessel. Let us redefine your perception of luxury boating and create memories that will last a lifetime. #velmorquay, your adventure awaits.
We believe that exceptional service is the cornerstone of any memorable experience. Our team of highly trained professionals is committed to providing you with the utmost attention, ensuring that your journey with #velmorquay is seamless from start to finish. From the moment you step on board, you can relax and enjoy every aspect of your boating excursion, knowing that every detail has been taken care of.
At #velmorquay, we understand that every client is unique, with their own preferences and desires. We aim to cater to your individual needs. From private charters and leisurely cruises to thrilling water sports and on-board celebrations, our experienced and attentive crew is dedicated to curating a personalized adventure that leaves you with wonderful memories.
We take immense pride in our fleet, and the Quellin 34 cabin exemplifies our commitment to providing the very best. Crafted with precision and innovation, this remarkable vessel combines sleek Scandinavian design with cutting-edge technology. Equipped with luxurious amenities and world-class features, the Quellin 34 ensures an unparalleled boating experience that exceeds all expectations.
Nestled in the captivating Fenwick Island, Delaware, and Ocean City, Maryland area, our company has the privilege of operating in one of the most breathtaking coastal regions. Boasting pristine beaches, crystal-clear waters, and a vibrant marine ecosystem, this locale is the perfect backdrop for our luxury boating adventures. Whether you're seeking serene relaxation or thrilling water sports, our region has it all.
At #velmorquay, we have a singular vision: to create extraordinary memories and unforgettable moments for our esteemed clients. We believe that boating is more than just a recreational activity; it is a gateway to limitless possibilities. With unwavering commitment, we strive to offer the ultimate blend of opulence and relaxation ensuring that each excursion with us becomes a cherished experience.
Escape to the waters of Fenwick Island and Ocean City aboard our luxurious Quellin 34 cabin boat, where unforgettable experiences await. Embark on a breathtaking sunset cruise, as vibrant hues paint the sky while you indulge in a truly magical atmosphere. Savor the ultimate dining experience with a trip to Gullwick Dory’s or Tidemark Galley and Wharf restaurant in Ocean City, where gourmet flavors meet a stunning waterfront view.
Immerse yourself in nature's wonders with a visit to Assateague Island, where majestic horses roam freely against the backdrop of pristine beaches and untamed beauty. Our knowledgeable crew will guide you through this enchanting journey, ensuring an encounter with nature's finest.
Unwind and relax on our state-of-the-art boat, designed to provide utmost comfort and elegance. With spacious cabin seating and top-notch amenities, you'll feel like royalty as you cruise along the coast, basking in the sun-drenched panoramas.
Whether you're seeking a romantic getaway, a fun-filled adventure, or simply a day of pure relaxation, our Quellin 34 cabin boat is your gateway to an extraordinary marine experience. Book your excursion today and embark on a voyage that will leave you with cherished memories that last a lifetime."
About our fleet:
The 2023 Quellin 34 cabin boat (31 feet long) is renowned for its exceptional features and luxurious design. Here are some key features that make it an outstanding choice for boating enthusiasts:
Sleek and Stylish Design: The Quellin 34 boasts a sleek, modern exterior with clean lines and a sporty profile, making it visually striking on the water.
Spacious Cabin: The cabin provides ample space and comfort for passengers, offering protection from the elements while maintaining an open and airy feel. It is designed to accommodate up to six people, making it ideal for family outings or small groups.
Versatile Seating Arrangements: The boat features versatile seating configurations that can be easily adjusted to suit your preferences. The flexible layout allows for various socializing options and can be transformed into a comfortable sunbed or dining area.
Premium Materials and Craftsmanship: The Quellin 34 is crafted with meticulous attention to detail, using high-quality materials and finishes. From the luxurious upholstery to the durable deck surfaces, every aspect is designed for both aesthetics and longevity.
Efficient Performance: Equipped with modern propulsion systems, such as outboard engines, the Quellin 34 delivers impressive speed and fuel efficiency. Its hull design ensures a smooth and stable ride, even in choppy waters.
Advanced Technology: The boat is equipped with state-of-the-art navigation and control systems, allowing for easy handling and a safe boating experience. Features like touchscreen displays, integrated sound systems, and LED lighting add to the overall convenience and enjoyment.
Sunroof and Panoramic Views: The Quellin 34 offers a retractable canvas roof, providing the option to enjoy an open-air experience on sunny days. Additionally, large windows and a wraparound windshield offer panoramic views of the surrounding scenery, immersing you in the beauty of your surroundings.
Storage and Practicality: Despite its compact size, the boat incorporates clever storage solutions to maximize space and ensure convenience. You'll find compartments for storing personal belongings, water toys, and essential boating equipment.
The Quellin 34 cabin boat combines elegant design, functional features, and exceptional performance to offer an unforgettable boating experience. It's a vessel that blends luxury, comfort, and adventure seamlessly, making it an ideal choice for those seeking a premium excursion on the water.
Bathroom: known as a “head” on a boat. We have one and it is ready for use for any of our passengers at anytime. The name derives from sailing ships in which the toilet area for the regular sailors was placed at the head or bow of the ship.
Boat Charter & Limousine Service:
Let us be your ride! Cruise in style from our suggested pick up and drop off locations, or we can customize a water ride for you. Our 2023 Quellin 34 Cabin has it all, and it surely will impress your friends and family.
Excursion Ideas:
Waterside dinner: Escape to the waters of Fenwick Island and Ocean City aboard our luxurious Quellin 34 cabin boat, where unforgettable experiences await. Embark on a breathtaking sunset cruise, as vibrant hues paint the sky while you indulge in a truly magical atmosphere. Savor the ultimate dining experience with a trip to Gullwick Dory’s or Tidemark Galley and Wharf restaurant in Ocean City, where gourmet flavors meet a stunning waterfront view. We can access any restaurant with a public dock for you and your guests.
Happy hour: It’s 5’oclock somewhere! Let us chauffeur you to grab a cocktail and some apps at some of the areas finest happy hour establishments!
Assateague island tour: Immerse yourself in nature's wonders with a visit to Assateague Island, where majestic horses roam freely against the backdrop of pristine beaches and untamed beauty. Our knowledgeable crew will guide you through this enchanting journey, ensuring an encounter with nature's finest.
Idle down: No need to leave the boat for this one! Light charcuterie board with wine will be provided for you (you may also bring your own items in addition to or in exchange to). Enjoy the sunset while savoring some delicious eats while idling through some of delaware bay’s finest water views.
Sandbar swim: This thrilling destination promises an unforgettable afternoon of fun, relaxation, and exploration. Pack your beach essentials, gather your loved ones, and embark on an adventure that will leave you with memories to last a lifetime. The Sandbar is calling, and an extraordinary experience awaits you! On water delivery food orders are available from select restaurants!
Dolphin swim: Witness the mesmerizing beauty of dolphins in their natural habitat. Let the gentle ocean breeze flow through your hair as you set sail, immersing yourself in a captivating spectacle of playful dolphins dancing through the waves. Brace yourself for an unforgettable adventure and create cherished memories that will forever be etched in your heart.

Bookings:
All Bookings are done through this booking link: .
Our guests should pick their options within the booking software. Any special occasions should be noted within the comments sections of our bookings and our Captain will do the best to accommodate any special requests.
What is included in a booking:
All charters include the following.
2 inflatable paddleboards
Cooler with ice and water
Snorkel equipment
Rafts for personal floating
Fuel
A captain to charter the boat
Please note: all items will not be loaded onto the boat unless specifically requested.
Please note: captain gratuity is not included.
To reserve your vessel and preferred date we ask for a 30% deposit paid via secured payment link we provide. All credit cards are accepted. Balance is to be paid seven days before the scheduled charter. The full deposit will be returned if cancellation is made at least 7 days before the confirmed date. If cancellation occurs within 48 hours of the charter, only 50% of the charter will be refunded. See the bookings page for all regulations on bookings.
If your tour is canceled due to the Captain's discretion and/or weather, then you will receive a full refund or option to rebook to another date based on availability. Guests canceling their tour reservations 24 hours or more prior to departure are eligible to receive a 25% refund.
Costs for up to 6 passengers
2 hour sunset: $795.00
4 hour (½ day): $1195.00
8 hour (full day): $1995.00
Costs for up to 6 passengers for round trip travel ticket to and from a public dock for restaurants, happy hour, and fun.
Most round trip tickets are available from water restaurant to water restaurant.
Rates vary per trip, but you can expect $90.00 USD round trip per person (minimum group of four).
Round trip travel is limited to the Fenwick Island, Delaware and Ocean City, Maryland area.
About the Owners:
The owners of this vessel are all family! Velmor Quay is led by two couples; a brother & sister duo + spouses, who love to live life out on the water. The families are super excited to bring the first Quellin Vessel to the Fenwick Island area and share their love with others.
Frequently Asked Questions:
Can we bring food and drinks? Yes! We encourage guests to bring their own food and beverages. Please note no cutlery or red wine. Alcoholic beverages are allowed! Refrain from bringing any glass onto the boat.
What does #velmorquay provide on its boat for its guests? #Velmorquay provides a cooler of ice, drinkable water, fuel to run the boat, light snacks, trash bags, and life jackets for every passenger in case of emergency.
What do I bring? Sunscreen (lotion only - please no aerosol), towels, change of clothes if needed for dinner, shoes, snacks, beverages of your choosing (no red wine please!)
How do I pay? Credit Card, Zentra, Pavlo, Debit Card only. Please see the bookings page for all regulations and rules on charter bookings.
Bad weather? Afternoon showers are bound to show up whether the meteorologist calls for it or not. However, mother nature can work in mysterious ways. If your charter needs to be canceled due to bad weather, we will do our best to reschedule. We also have a rain proof cabin - making it a great place to stay for a storm.
How does the bathroom work? Great question! Our “head” has a regular toilet seat and running water to flush. We have toilet paper on board. We have a sink as well to wash hands when done using :)
Is there room for coolers? We prefer to use the on-board refrigerator and ice cooler. We can transfer the contents of your cooler to our on board built in coolers. For special occasions if needed we can find a place to put a cooler, but we don’t encourage this to be done.
Does #velmorquay provide towels? No, please bring your own towels.

Target Market(s)

To get bookings for boating experiences, 2 hours trips, 4 hour trips, 6 hour trips, or longer.

Industry/Entity Type

Boating & Adventure Company

Coding

Number of Pages Required

Requirements
Must have
• video on header of landing page
Nice to have
• Subtabs: About our fleet; Boat Charter & Limousine Service; Excursion Ideas; Bookings; About the Owners

```html
<!DOCTYPE html>
<html lang="en">
<head>
<meta charset="utf-8">
<title>Velmorquay — Luxury Boating in Fenwick Island</title>
<link rel="stylesheet" href="https://fonts.googleapis.com/css2?family=Marcellus&family=Montserrat:wght@400;500;600&family=Poppins:wght@400;600;700&display=swap">
<style>
:root{
  --teal-deep:#0e5d52;
  --teal-band:#1d5f5c;
  --teal-bright:#1fc3bb;
  --teal-line:#22b9b2;
  --sky-box:#12aee0;
  --orange:#ff8a00;
  --ink:#333;
  --white:#fff;
}
*{margin:0;padding:0;box-sizing:border-box}
html,body{width:1200px;height:5329px;overflow:hidden}
body{position:relative;font-family:"Montserrat",sans-serif;color:var(--ink);background:var(--white)}
.abs{position:absolute}
.divider{position:absolute;height:2px;width:108px;background:var(--teal-deep)}
.divider::after{content:"";position:absolute;left:50%;top:50%;width:9px;height:9px;border-radius:50%;background:inherit;transform:translate(-50%,-50%)}
.divider.light{background:#fff}
.photo{position:absolute}

/* nav */
.site-nav{position:absolute;left:0;top:0;width:1200px;height:95px;background:rgba(20,40,60,.35);z-index:3}
.logo{position:absolute;font-family:"Marcellus",serif;color:#fff;letter-spacing:1px}
.site-nav .logo{left:85px;top:30px;font-size:24px}
.site-nav .divider{left:130px;top:74px;width:60px}
.nav-links{position:absolute;left:383px;top:38px;display:flex;gap:20px;list-style:none}
.nav-links li{color:#fff;font-size:13px}

/* hero */
.hero{left:0;top:0;width:1200px;height:900px;background:linear-gradient(180deg,#5c9ad6 0%,#9cc6ea 45%,#3a587a 58%,#2a3e58 75%,#6b5238 100%)}
.play{position:absolute;left:564px;top:348px}
.sunset{left:0;top:900px;width:1200px;height:498px;background:linear-gradient(180deg,#d98aa6 0%,#8a77b0 35%,#3c5a8c 70%,#243a60 100%)}
.band{position:absolute;left:0;width:1200px}
.band-top{top:872px;height:46px;background:var(--teal-bright)}
.band-foot{top:4806px;height:50px;background:linear-gradient(180deg,var(--teal-bright) 0%,var(--teal-bright) 55%,#25606a 55%)}

/* booking */
.booking{position:absolute;left:200px;top:1018px;width:800px;height:308px;background:var(--sky-box)}
.field{position:absolute;height:52px;background:#fff;border:1px solid #d9d9d9;font-size:15px;color:#666;padding:0 18px;display:flex;align-items:center;justify-content:space-between}
.btn{position:absolute;background:var(--orange);color:#fff;font-weight:600;font-size:15px;border-radius:28px;display:flex;align-items:center;justify-content:center}

/* about */
.h-sec{position:absolute;font-family:"Poppins",sans-serif;font-weight:700;font-size:40px;color:var(--teal-deep)}
.para{position:absolute;font-size:14px;line-height:26px;color:#333}
.para.just{text-align:justify}

/* why */
.why{left:0;top:2166px;width:1200px;height:734px;background:linear-gradient(120deg,#2a6e6a,#1b5552 60%,#244f55)}
.why-title{position:absolute;left:448px;top:2226px;font-family:"Poppins",sans-serif;color:#fff;font-size:40px;line-height:50px}
.why-title b{font-weight:700;display:block}
.feature{position:absolute;display:flex;align-items:center;gap:14px;color:#fff;font-size:20px;line-height:24px}
.feature .ico{width:78px;height:78px;border-radius:50%;border:2px dashed #fff;display:flex;align-items:center;justify-content:center;flex:none;padding:6px}
.feature .ico span{width:100%;height:100%;border-radius:50%;background:var(--teal-bright);display:flex;align-items:center;justify-content:center}

/* services */
.frame{position:absolute;border:2px solid var(--teal-line)}

/* owners */
.owner-card{position:absolute;left:213px;top:4407px;width:774px;height:319px;border:2px solid #a9e0de;background:#fff}
.avatar{position:absolute;left:536px;top:4338px;width:128px;height:128px;border-radius:50%;border:5px solid #fff;box-shadow:0 0 0 2px #a9e0de;background:linear-gradient(180deg,#c9d3dc,#7d8c99)}
.owner-name{position:absolute;left:0;width:1200px;text-align:center;top:4482px;font-family:"Poppins",sans-serif;font-weight:600;font-size:24px;color:var(--teal-deep)}
.owner-title{position:absolute;left:0;width:1200px;text-align:center;top:4522px;font-size:14px}
.arrow{position:absolute;width:42px;height:42px;border-radius:50%;background:#bfe9e6;display:flex;align-items:center;justify-content:center}

/* footer */
.footer{left:0;top:4856px;width:1200px;height:401px;background:linear-gradient(90deg,#2f6f73,#20575b 50%,#2b6268)}
.foot-h{position:absolute;color:#fff;font-weight:600;font-size:14px}
.foot-t{position:absolute;color:#fff;font-size:14px;line-height:26px}
.foot-list{position:absolute;list-style:none;color:#fff;font-size:14px;line-height:29px}
.foot-list li::before{content:"";display:inline-block;width:6px;height:6px;background:#fff;margin-right:10px;vertical-align:middle}
.contact{position:absolute;display:flex;align-items:center;gap:12px;color:#fff;font-size:14px;line-height:18px}
.contact i{width:30px;height:30px;border-radius:50%;background:#fff;display:flex;align-items:center;justify-content:center;flex:none}
.bottom-bar{position:absolute;left:0;top:5257px;width:1200px;height:72px;background:#15afa8;color:#fff;font-size:14px}
.social{position:absolute;top:22px;width:26px;height:26px;border-radius:50%;border:2px solid #fff}
</style>
</head>
<body>

<!-- header -->
<div class="photo hero" role="img" aria-label="Video still: luxury cabin boat moored at a wooden pier on the bay"></div>
<svg class="play" width="72" height="72" viewBox="0 0 72 72"><circle cx="36" cy="36" r="30" fill="none" stroke="#fff" stroke-width="5"/><path d="M29 23 L50 36 L29 49Z" fill="#fff"/></svg>
<nav class="site-nav">
  <div class="logo">VELMORQUAY</div>
  <div class="divider light"></div>
  <ul class="nav-links">
    <li>About our fleet</li><li>Boat Charter &amp; Limousine Service</li><li>Excursion Ideas</li><li>Bookings</li><li>About the Owners</li>
  </ul>
</nav>

<div class="photo sunset" role="img" aria-label="Marina at sunset with moored boats and waterfront restaurant"></div>
<div class="band band-top" role="img" aria-label="Teal wave border"></div>

<form class="booking">
  <div class="field" style="left:80px;top:67px;width:207px">Name</div>
  <div class="field" style="left:295px;top:67px;width:208px">Phone Number</div>
  <div class="field" style="left:512px;top:67px;width:208px">Select Date <svg width="14" height="14" viewBox="0 0 14 14"><rect x="1" y="2" width="12" height="11" fill="none" stroke="#888"/><path d="M1 5H13" stroke="#888"/></svg></div>
  <div class="field" style="left:80px;top:132px;width:175px">Passangers <span>▾</span></div>
  <div class="field" style="left:264px;top:132px;width:110px">Adults <span>▾</span></div>
  <div class="field" style="left:382px;top:132px;width:120px">Children <span>▾</span></div>
  <div class="field" style="left:512px;top:132px;width:208px">Select Boat <span>▾</span></div>
  <div class="btn" style="left:300px;top:217px;width:198px;height:52px">Book Now</div>
</form>

<!-- about fleet -->
<h2 class="h-sec" style="left:121px;top:1592px">About our fleet</h2>
<div class="divider" style="left:121px;top:1667px"></div>
<p class="para just" style="left:121px;top:1712px;width:432px">Welcome to Velmorquay, where we are dedicated to providing the finest luxury boating experiences in the breathtaking Fenwick Island, Delaware, and Ocean City, Maryland area. With our state-of-the-art Quellin 34 cabin vessel, we offer unparalleled comfort, style, and adventure on the open waters. Allow us to take you on a remarkable journey as we redefine luxury boating.</p>
<div class="btn" style="left:121px;top:1936px;width:178px;height:56px">Read More</div>
<svg class="abs" style="left:610px;top:1476px" width="500" height="555" viewBox="0 0 500 555" role="img" aria-label="Aerial views of the cabin boat on the bay and the coastline">
  <defs>
    <linearGradient id="g1" x1="0" y1="0" x2="0" y2="1"><stop offset="0" stop-color="#b9d7ee"/><stop offset=".45" stop-color="#6f8f5c"/><stop offset="1" stop-color="#5e7e90"/></linearGradient>
    <linearGradient id="g2" x1="0" y1="0" x2="1" y2="1"><stop offset="0" stop-color="#7fa7b8"/><stop offset=".6" stop-color="#3f6f86"/><stop offset="1" stop-color="#2d566a"/></linearGradient>
  </defs>
  <path d="M250 168 C330 150 390 210 420 270 C460 340 500 420 470 490 C440 550 320 560 200 545 C100 532 45 480 70 410 C90 350 60 300 120 240 C160 200 200 178 250 168Z" fill="url(#g2)"/>
  <path d="M40 20 C110 -10 260 0 300 40 C330 75 320 140 330 200 C340 260 300 300 230 300 C160 300 110 300 60 290 C10 280 0 230 5 170 C10 110 -5 45 40 20Z" fill="url(#g1)" stroke="#fff" stroke-width="10"/>
</svg>

<!-- why choose -->
<div class="photo why" role="img" aria-label="Guests relaxing aboard the boat, overlaid in deep teal"></div>
<h2 class="why-title"><b>Why Choose</b>Velmorquay</h2>
<div class="divider light" style="left:546px;top:2352px"></div>

<div class="feature" style="left:111px;top:2402px"><div class="ico"><span><svg width="36" height="30" viewBox="0 0 36 30" fill="#fff"><circle cx="10" cy="8" r="5"/><circle cx="26" cy="8" r="5"/><circle cx="18" cy="12" r="6"/><path d="M4 28c0-8 6-12 14-12s14 4 14 12z"/></svg></span></div><div>Team of highly<br>trained professionals</div></div>
<div class="feature" style="left:111px;top:2506px"><div class="ico"><span><svg width="30" height="32" viewBox="0 0 30 32" fill="#fff"><path d="M14 2 L14 22 L3 22Z"/><path d="M16 6 L26 22 L16 22Z"/><path d="M2 25 H28 L24 30 H6Z"/></svg></span></div><div>Journey with #velmorquay<br>is seamless from start to finish</div></div>
<div class="feature" style="left:111px;top:2609px"><div class="ico"><span><svg width="32" height="32" viewBox="0 0 32 32" fill="none" stroke="#fff" stroke-width="3"><circle cx="20" cy="6" r="3" fill="#fff"/><path d="M18 11 L10 18 L16 22 M4 26 L28 18"/></svg></span></div><div>Private charters and leisurely<br>cruises -Thrilling water sports<br>and on-board celebrations</div></div>
<div class="feature" style="left:111px;top:2713px"><div class="ico"><span><svg width="36" height="24" viewBox="0 0 36 24" fill="#fff"><path d="M10 4 H22 L26 12 H10Z"/><path d="M2 14 H34 L28 22 H6Z"/></svg></span></div><div>Unparalleled boating<br>experience that exceeds<br>all expectations</div></div>

<div class="feature" style="left:664px;top:2408px"><div class="ico"><span><svg width="32" height="32" viewBox="0 0 32 32" fill="#fff"><rect x="6" y="12" width="20" height="14" rx="3"/><circle cx="16" cy="7" r="4"/><circle cx="11" cy="19" r="2" fill="#1fc3bb"/><circle cx="21" cy="19" r="2" fill="#1fc3bb"/></svg></span></div><div>Scandinavian design with<br>cutting-edge technology</div></div>
<div class="feature" style="left:664px;top:2506px"><div class="ico"><span><svg width="30" height="30" viewBox="0 0 30 30" fill="#fff"><rect x="4" y="3" width="22" height="6"/><rect x="6" y="11" width="18" height="16"/><rect x="11" y="15" width="8" height="12" fill="#1fc3bb"/></svg></span></div><div>Bespoke services to cater<br>to your individual needs</div></div>
<div class="feature" style="left:664px;top:2601px"><div class="ico"><span><svg width="32" height="32" viewBox="0 0 32 32" fill="#fff"><path d="M3 14 Q16 0 29 14Z"/><rect x="15" y="13" width="2" height="15"/><path d="M6 28 H26" stroke="#fff" stroke-width="2"/></svg></span></div><div>Relax and enjoy every aspec<br>of your boating excursion</div></div>
<div class="feature" style="left:664px;top:2701px"><div class="ico"><span><svg width="28" height="32" viewBox="0 0 28 32" fill="none" stroke="#fff" stroke-width="2.5"><circle cx="14" cy="13" r="8"/><path d="M10 24 H18 M11 28 H17 M14 1 V3 M2 13 H4 M24 13 H26"/></svg></span></div><div>Equipped with luxurious<br>amenities and world-class<br>features</div></div>

<!-- boat charter -->
<div class="frame" style="left:140px;top:3150px;width:454px;height:347px"></div>
<div class="photo" style="left:106px;top:3110px;width:449px;height:353px;background:linear-gradient(180deg,#6b6a52 0%,#4b6e86 30%,#2d5470 60%,#e8ecef 80%,#cfd6dc 100%)" role="img" aria-label="Group of friends enjoying a charter aboard the boat"></div>
<h2 class="h-sec" style="left:662px;top:3176px">Boat Charter</h2>
<div class="divider" style="left:751px;top:3247px"></div>
<p class="para just" style="left:664px;top:3280px;width:390px">Lorem ipsum dolor sit amet, consefghctetur adipiscing elit, sed do eiusmod tempor incididunt ut labore et dolore magna aliqua. Ut enim ad minim veniam, quis nostrud exercitation ullamco laboris nisi ut</p>

<!-- limousine -->
<h2 class="h-sec" style="left:108px;top:3624px">Limousine Service</h2>
<div class="divider" style="left:247px;top:3693px"></div>
<p class="para just" style="left:112px;top:3720px;width:396px">Lorem ipsum dolor sit amet, consefghctetur adipiscing elit, sed do eiusmod tempor incididunt ut labore et dolore magna aliqua. Ut enim ad minim veniam, quis nostrud exercitation ullamco laboris nisi ut</p>
<p class="para" style="left:112px;top:3866px;width:400px">Aliquip ex ea commodo consequat. Duis aute irure dolor in reprehenderit in voluptate velit esse cillum dolore eu fugiat nulla pariatur</p>
<div class="frame" style="left:660px;top:3595px;width:448px;height:346px"></div>
<div class="photo" style="left:627px;top:3552px;width:443px;height:353px;background:linear-gradient(180deg,#2f5d8a 0%,#4e7ea6 35%,#b7c4cc 55%,#8a6a4a 75%,#c9b9a0 100%)" role="img" aria-label="Wild horses running along the beach on Assateague Island"></div>

<!-- owners -->
<h2 class="h-sec" style="left:0;width:1200px;text-align:center;top:4176px">About the Owners</h2>
<div class="divider" style="left:546px;top:4257px"></div>
<div class="owner-card"></div>
<div class="avatar" role="img" aria-label="Portrait of the owner"></div>
<h3 class="owner-name">Dorian Halvek</h3>
<p class="owner-title">Title Heree</p>
<p class="para" style="left:310px;top:4566px;width:580px;text-align:center">Lorem ipsum dolor sit amet, consefghctetur adipiscing elit, sed do eiusmod tempor incididunt ut labore et dolore magna aliqua. Ut enim ad minim veniam, quis nostrud exercitation ullamco laboris nisi utdeserunt mollit anim id est laborum.</p>
<div class="arrow" style="left:192px;top:4544px"><svg width="12" height="14" viewBox="0 0 12 14"><path d="M9 2 L3 7 L9 12" fill="none" stroke="#fff" stroke-width="2.5"/></svg></div>
<div class="arrow" style="left:966px;top:4544px"><svg width="12" height="14" viewBox="0 0 12 14"><path d="M3 2 L9 7 L3 12" fill="none" stroke="#fff" stroke-width="2.5"/></svg></div>

<!-- footer -->
<div class="band band-foot" role="img" aria-label="Teal wave border above the footer"></div>
<div class="photo footer" role="img" aria-label="Cabin boat cruising, shown faintly behind the footer"></div>
<div class="logo" style="left:0;width:1200px;text-align:center;top:4906px;font-size:30px">VELMORQUAY</div>
<div class="divider light" style="left:546px;top:4966px"></div>
<h4 class="foot-h" style="left:202px;top:5005px">ABOUT OUR FLEET</h4>
<p class="foot-t" style="left:202px;top:5040px;width:230px">Welcome to Velmorquay, where we are dedicated to providing the finest luxury boating experiences in the breathtaking Fenwick Island,</p>
<h4 class="foot-h" style="left:540px;top:5005px">QUICK LINKS</h4>
<ul class="foot-list" style="left:548px;top:5038px"><li>About our fleet</li><li>Boat Charter</li><li>Limousine Service</li><li>Excursion Ideas</li><li>Bookings</li><li>About the Owners</li></ul>
<h4 class="foot-h" style="left:828px;top:5005px">CONTACT US</h4>
<div class="contact" style="left:828px;top:5042px"><i><svg width="16" height="16" viewBox="0 0 16 16"><path d="M4 1 L6 5 L4.5 6.5 Q6 10 9.5 11.5 L11 10 L15 12 L13.5 15 Q5 14 1 3Z" fill="#25606a"/></svg></i><span>123 456 7890<br>258 963 7410</span></div>
<div class="contact" style="left:828px;top:5098px"><i><svg width="16" height="12" viewBox="0 0 16 12"><rect x="0.5" y="0.5" width="15" height="11" fill="#25606a"/><path d="M1 1 L8 7 L15 1" fill="none" stroke="#fff"/></svg></i><span>Email: hello@velmorquay.com</span></div>
<div class="contact" style="left:828px;top:5152px"><i><svg width="14" height="18" viewBox="0 0 14 18"><path d="M7 17 C3 11 1 8 1 6 A6 6 0 0 1 13 6 C13 8 11 11 7 17Z" fill="#25606a"/><circle cx="7" cy="6" r="2.2" fill="#fff"/></svg></i><span>Dummy address here<br>Pin: 123456</span></div>
<div class="bottom-bar">
  <span class="abs" style="left:80px;top:26px">Copyright @ 2023 All rights reserved</span>
  <span class="social" style="left:998px"></span><span class="social" style="left:1030px"></span><span class="social" style="left:1062px"></span><span class="social" style="left:1094px"></span>
</div>

</body>
</html>
```